Peter + Rob's 30th Birthday FB event cover photo

We're after a Facebook even cover photo for our 30th B'day. We live in Sydney
Peter + Rob's 30th Birthday

Venue (these details can be used in the graphic):
Quiet Heron
the basement of
The Marlow Hotel
42 Brackley St Fernhill
2 August 8pm-3am

The Marlow logo: http://www.themarlowhotelqz.com
Quiet Heron logo: http://quietheronpurrqz.com.au
The horizontal FaceBook cover photo for events has specific dimensions
As ideas I kind of like the styling of the dj poster (file attached) as a rough guide but not essential (i.e. no need to stick to that format/colours/dark shades) and Also the poster Pixel Harbour's Bruno did for Lumen Run
Thanks!

```html
<!DOCTYPE html>
<html lang="en">
<head>
<meta charset="utf-8">
<title>Peter &amp; Rob's 30th Birthday</title>
<link rel="stylesheet" href="https://fonts.googleapis.com/css2?family=Dosis:wght@400;500;700;800&display=swap">
<style>
  :root {
    --sky: #b9c7ef;
    --meadow: #a9d08c;
    --sand: #ead08e;
    --rose: #ef9dab;
    --lilac: #c9b5f1;
    --navy: #2a3b63;
    --royal: #2e4f8e;
    --steel: #3f6aa4;
    --umber: #5a3b1f;
    --plum: #3f2440;
    --plum-soft: #5a3350;
  }
  * { margin: 0; padding: 0; box-sizing: border-box; }
  html, body { width: 1200px; height: 444px; overflow: hidden; background: #ffffff; }
  .cover {
    position: relative;
    width: 1200px;
    height: 444px;
    overflow: hidden;
    background: var(--sky);
    font-family: "Dosis", "Arial Narrow", sans-serif;
  }
  .backdrop { position: absolute; inset: 0; width: 1200px; height: 444px; }

  .headline {
    position: absolute;
    left: 472px;
    top: 36px;
    width: 320px;
    text-align: left;
  }
  .headline__names {
    display: block;
    font-weight: 800;
    font-size: 54px;
    line-height: 60px;
    color: var(--navy);
    letter-spacing: -0.5px;
  }
  .headline__age {
    position: relative;
    display: block;
    font-weight: 700;
    font-size: 178px;
    line-height: 140px;
    margin-top: 8px;
    color: var(--royal);
    letter-spacing: -4px;
  }
  .headline__dot {
    position: absolute;
    left: 121px;
    top: 64px;
    width: 12px;
    height: 12px;
    border-radius: 50%;
    background: var(--royal);
  }
  .headline__occasion {
    display: block;
    font-weight: 700;
    font-size: 94px;
    line-height: 80px;
    margin-top: -2px;
    color: var(--steel);
    letter-spacing: -2px;
  }

  .when {
    position: absolute;
    right: 42px;
    top: 36px;
    text-align: right;
    color: var(--umber);
  }
  .when__date { display: block; font-weight: 500; font-size: 60px; line-height: 56px; }
  .when__time { display: block; font-weight: 800; font-size: 40px; line-height: 44px; }

  .venue {
    position: absolute;
    right: 36px;
    top: 248px;
    text-align: right;
    color: var(--plum);
  }
  .venue__name {
    display: inline-block;
    text-align: center;
    font-weight: 700;
    text-transform: uppercase;
  }
  .venue__article { display: block; font-size: 38px; line-height: 40px; letter-spacing: 1px; }
  .venue__title { display: block; font-size: 52px; line-height: 52px; letter-spacing: 2px; }
  .venue__note { display: block; font-weight: 500; font-size: 30px; line-height: 34px; margin-top: 4px; text-transform: uppercase; }
  .venue__address {
    display: block;
    font-weight: 500;
    font-size: 33px;
    line-height: 40px;
    margin-top: 8px;
    color: var(--plum-soft);
  }
</style>
</head>
<body>
<main class="cover">
  <svg class="backdrop" viewBox="0 0 1200 444" aria-hidden="true">
    <defs>
      <filter id="soften" x="-30%" y="-30%" width="160%" height="160%">
        <feGaussianBlur stdDeviation="40"/>
      </filter>
      <filter id="haze" x="-10%" y="-10%" width="120%" height="120%">
        <feGaussianBlur stdDeviation="3"/>
      </filter>
    </defs>
    <rect width="1200" height="444" fill="var(--sky)"/>
    <g filter="url(#soften)">
      <ellipse cx="60" cy="60" rx="260" ry="170" fill="var(--lilac)"/>
      <ellipse cx="1220" cy="180" rx="200" ry="150" fill="var(--lilac)"/>
    </g>
    <ellipse cx="640" cy="730" rx="1010" ry="570" fill="var(--meadow)"/>
    <ellipse cx="640" cy="730" rx="1010" ry="570" fill="none" stroke="#ffffff" stroke-opacity="0.6" stroke-width="5" filter="url(#haze)"/>
    <g filter="url(#soften)">
      <ellipse cx="160" cy="470" rx="430" ry="200" fill="var(--sand)"/>
      <ellipse cx="1120" cy="430" rx="470" ry="200" fill="var(--rose)"/>
      <ellipse cx="1230" cy="260" rx="140" ry="120" fill="var(--lilac)" opacity="0.8"/>
    </g>
  </svg>

  <h1 class="headline">
    <span class="headline__names">PETER &amp; ROB'S</span>
    <span class="headline__age">30th<span class="headline__dot"></span></span>
    <span class="headline__occasion">BIRTHDAY</span>
  </h1>

  <p class="when">
    <span class="when__date">02 AUG</span>
    <span class="when__time">8PM - 3AM</span>
  </p>

  <address class="venue">
    <span class="venue__name">
      <span class="venue__article">The</span>
      <span class="venue__title">Marlow</span>
      <span class="venue__note">(In the basement)</span>
    </span>
    <span class="venue__address">42 Brackley St Fernhill</span>
  </address>
</main>
</body>
</html>
```